KerrLow Farm

Need a nice simple clean double sided business card that has our logo and info on:
Kerr Low Farm
Martin & Felicity Kerr Low
kerrlowfarm@mailbarn.example
Martin: 1-780-555-0148
Felicity: 1-780-555-0193
Instagram @ kerrlow_farm

Contact Information for Business Card

Martin & Felicity Kerr Low kerrlowfarm@mailbarn.example Martin: 1-780-555-0148 Felicity: 1-780-555-0193

```html
<!DOCTYPE html>
<html lang="en">
<head>
<meta charset="utf-8">
<title>Kerr Low Farm – Business Card</title>
<link rel="stylesheet" href="https://fonts.googleapis.com/css2?family=Libre+Baskerville:wght@400;700&family=Montserrat:wght@400;500&display=swap">
<style>
  :root {
    --farm-green: #5c9a04;
    --harvest-orange: #fba50a;
    --paper-white: #ffffff;
    --backdrop: #d9d9d9;
    --card-shadow: rgba(0,0,0,0.22);
  }
  * { box-sizing: border-box; margin: 0; padding: 0; }
  html, body { width: 1200px; height: 800px; overflow: hidden; }
  body {
    background: var(--backdrop);
    position: relative;
    font-family: "Montserrat", Arial, sans-serif;
  }
  .card {
    position: absolute;
    left: 320px;
    width: 560px;
    height: 320px;
    border-radius: 18px;
    overflow: hidden;
    box-shadow: 0 10px 28px var(--card-shadow);
  }
  .card--front { top: 50px; background: var(--paper-white); }
  .card--back { top: 430px; background: var(--harvest-orange); }

  .card__art { position: absolute; inset: 0; }

  .wheat-stalk {
    position: absolute;
    left: 279px;
    top: 16px;
    width: 16px;
    height: 90px;
    border-radius: 8px;
    background: linear-gradient(180deg, rgba(251,165,10,0.3), var(--harvest-orange));
  }

  .contact-block {
    position: absolute;
    left: 30px;
    top: 78px;
    width: 230px;
  }
  .contact-block__names {
    font-family: "Libre Baskerville", Georgia, serif;
    font-weight: 700;
    font-size: 17px;
    line-height: 1.15;
    color: var(--harvest-orange);
    text-transform: uppercase;
    margin-bottom: 14px;
  }
  .contact-list { list-style: none; }
  .contact-list__item {
    display: flex;
    align-items: center;
    gap: 8px;
    color: var(--paper-white);
    font-size: 11.5px;
    font-weight: 500;
    line-height: 1;
    margin-bottom: 8px;
    white-space: nowrap;
  }
  .contact-list__icon { width: 12px; height: 12px; flex: none; }
  .contact-list__who { font-style: italic; font-weight: 400; }

  .brand-lockup {
    position: absolute;
    left: 305px;
    top: 86px;
    width: 245px;
    text-align: center;
  }
  .brand-lockup__circle {
    width: 54px;
    height: 54px;
    border: 3px solid var(--farm-green);
    border-radius: 50%;
    margin: 0 auto 12px;
  }
  .brand-lockup__name {
    font-family: "Libre Baskerville", Georgia, serif;
    font-weight: 400;
    font-size: 22px;
    color: var(--farm-green);
    text-transform: uppercase;
    letter-spacing: 0.5px;
  }
  .brand-lockup__tagline {
    margin-top: 8px;
    font-size: 10px;
    letter-spacing: 6px;
    color: var(--harvest-orange);
    text-transform: uppercase;
  }

  .back-mark {
    position: absolute;
    left: 195px;
    top: 45px;
    width: 170px;
    height: 170px;
    border: 5px solid var(--paper-white);
    border-radius: 50%;
    display: flex;
    align-items: center;
    justify-content: center;
  }
  .back-mark__name {
    font-family: "Libre Baskerville", Georgia, serif;
    font-weight: 400;
    font-size: 19px;
    line-height: 1.3;
    color: var(--paper-white);
    text-align: center;
    text-transform: uppercase;
  }
  .back-web {
    position: absolute;
    left: 0;
    right: 0;
    top: 252px;
    text-align: center;
    font-family: "Libre Baskerville", Georgia, serif;
    font-size: 13px;
    letter-spacing: 2.5px;
    color: var(--paper-white);
  }
</style>
</head>
<body>

  <section class="card card--front" aria-label="Business card front">
    <svg class="card__art" viewBox="0 0 560 320" width="560" height="320" aria-hidden="true">
      <path d="M0,0 H232 C300,95 300,230 268,320 H0 Z" fill="var(--farm-green)"/>
      <path d="M284,110 C306,180 308,255 298,320 L290,320 C298,255 298,185 284,110 Z" fill="var(--harvest-orange)"/>
    </svg>
    <div class="wheat-stalk" role="img" aria-label="Wheat stalk illustration in orange"></div>

    <div class="contact-block">
      <h1 class="contact-block__names">Martin &amp;<br>Felicity Kerr Low</h1>
      <ul class="contact-list">
        <li class="contact-list__item">
          <svg class="contact-list__icon" viewBox="0 0 12 12"><rect x="3" y="0.5" width="6" height="11" rx="1.2" fill="none" stroke="var(--harvest-orange)" stroke-width="1.3"/></svg>
          1-780-555-0148 <span class="contact-list__who">Martin</span>
        </li>
        <li class="contact-list__item">
          <svg class="contact-list__icon" viewBox="0 0 12 12"><rect x="3" y="0.5" width="6" height="11" rx="1.2" fill="none" stroke="var(--harvest-orange)" stroke-width="1.3"/></svg>
          1-780-555-0193 <span class="contact-list__who">Felicity</span>
        </li>
        <li class="contact-list__item">
          <svg class="contact-list__icon" viewBox="0 0 12 12"><rect x="0.5" y="2" width="11" height="8" fill="var(--harvest-orange)"/><path d="M0.5,2 L6,6.5 L11.5,2" fill="none" stroke="var(--farm-green)" stroke-width="1"/></svg>
          kerrlowfarm@mailbarn.example
        </li>
        <li class="contact-list__item">
          <svg class="contact-list__icon" viewBox="0 0 12 12"><rect x="1" y="1" width="10" height="10" fill="none" stroke="var(--harvest-orange)" stroke-width="1.3"/></svg>
          @kerrlow_farm
        </li>
      </ul>
    </div>

    <div class="brand-lockup">
      <div class="brand-lockup__circle"></div>
      <p class="brand-lockup__name">Kerr Low Farm</p>
      <p class="brand-lockup__tagline">Stone Milled Flour</p>
    </div>
  </section>

  <section class="card card--back" aria-label="Business card back">
    <div class="back-mark">
      <p class="back-mark__name">Kerr Low<br>Farm</p>
    </div>
    <p class="back-web">WWW.KERRLOWFARM.EXAMPLE</p>
  </section>

</body>
</html>
```